Farhan Jewellers Stationary Contest

Pakistan’s largest Jewellery, Diamond and luxury watches store requires professional stationery. We have a long list of are trusted clients since 1959, our third generation has successfully maintained and sustained the legacy and excellence in the sector.

We require stationery template as part of this contest. The stationery can be double sided.

We prefer a design that makes use of some of the premium business stationery printing options, such as foil stamping, embossing/debossing, painted edges, spot UV etc (doesn't have to use all these options, only what you feel works, but we are looking for a design that stands out and is memorable and these nice touches have that effect.)

We want an eye catching, innovative, high end professional looking stationery for an out of box design that blends well with our new logo (attached). We want the design to be an out of box solution, you may use any element to compliment the logo. You may consider incorporating watermark etc, highlighting our products (Gold and Diamond Jewellery in addition to Luxury watches)

Company details are as follows;

Company name: Farhan Jewellers
Contact Person: Tariq Naveed
Designation: Business Development Consultant
Mobile: +92 333 815 6042
Email: tariqnaveed@mailvora.com
Website: www.farhanjewellers-pk.net

Target Market(s)

Matrimonial, Elite & Businesses class, Upmarket

Font styles to use
Other font styles liked:
• Designers choice

Colors

Designer to choose colors to be used in the design.

Requirements
Must have
• Look and feel: Upmarket, innovative, Modern, Professional, graceful, Elegant, designer stuff.
Nice to have
• Unique design

```html
<!DOCTYPE html>
<html lang="en">
<head>
<meta charset="utf-8">
<title>Farhan Jewellers Stationery</title>
<link rel="stylesheet" href="https://fonts.googleapis.com/css2?family=Montserrat:wght@700&family=Carlito&family=Tinos&display=swap">
<style>
:root{
  --gold:#d9a21a;
  --gold-light:#f1c232;
  --black:#0b0b0b;
  --paper:#ffffff;
  --ink:#2a2a2a;
  --backdrop:#e9e9e9;
  --brand:"Montserrat",sans-serif;
  --body:"Carlito",sans-serif;
  --detail:"Tinos",serif;
}
*{margin:0;padding:0;box-sizing:border-box}
html,body{width:1200px;height:1200px;overflow:hidden}
body{background:var(--backdrop);position:relative;font-family:var(--body)}
.piece{position:absolute;overflow:hidden}
.brand-name{font-family:var(--brand);font-weight:700;color:var(--gold);white-space:nowrap;letter-spacing:.02em}
.brand-dot{display:block;border-radius:50%;background:var(--gold);margin:0 auto}

/* Letterhead */
.letterhead{left:91px;top:22px;width:480px;height:624px;background:var(--paper)}
.letterhead .header-block{position:absolute;right:0;top:0;width:115px;height:86px;background:var(--black);display:flex;flex-direction:column;align-items:center;justify-content:center;gap:6px}
.letterhead .header-block .brand-dot{width:12px;height:12px}
.letterhead .header-block .brand-name{font-size:9px}
.letter-body{position:absolute;left:29px;top:204px;width:430px;font-size:10.2px;line-height:14px;color:var(--ink)}
.letter-body p{margin-bottom:14px}
.letter-footer{position:absolute;left:0;bottom:10px;display:flex;gap:8px;align-items:stretch}
.letter-footer .bar{width:13px;background:var(--gold)}
.letter-footer .lines{font-family:var(--detail);font-size:6.8px;line-height:8.4px;color:var(--gold);padding:2px 0}

/* Presentation folder */
.folder{left:600px;top:60px;width:509px;height:679px;background:var(--black)}
.folder svg.cut{position:absolute;left:0;top:0}
.folder .mark{position:absolute;left:0;right:0;top:102px;text-align:center}
.folder .mark .brand-dot{width:40px;height:40px;margin-bottom:34px}
.folder .mark .brand-name{font-size:31px}
.folder .site{position:absolute;left:0;right:0;top:652px;text-align:center;font-family:var(--detail);font-size:9.5px;letter-spacing:.28em;color:var(--gold)}

/* Business cards */
.card{top:667px;width:195px;height:113px;background:var(--black)}
.card svg{position:absolute;left:0;top:0}
.card-front{left:121px}
.card-back{left:344px}
.card-front .mark{position:absolute;left:8px;top:26px;width:70px;text-align:center}
.card-front .mark .brand-dot{width:10px;height:10px;margin-bottom:6px}
.card-front .mark .brand-name{font-size:6px}
.card-front .person{position:absolute;right:10px;top:36px;text-align:right;font-family:var(--detail);color:var(--gold)}
.card-front .person .name{font-size:12px;line-height:13px}
.card-front .person .role{font-size:3.6px;line-height:6px;margin-bottom:3px}
.card-front .person .line{font-size:6px;line-height:6.6px}
.card-front .address{position:absolute;left:26px;bottom:4px;font-family:var(--detail);font-size:5.4px;color:var(--black)}
.card-back .mark{position:absolute;left:0;right:0;top:32px;text-align:center}
.card-back .mark .brand-dot{width:12px;height:12px;margin-bottom:8px}
.card-back .mark .brand-name{font-size:10px}
.card-back .site{position:absolute;left:8px;bottom:3px;font-family:var(--detail);font-size:5.4px;color:var(--black)}

/* Envelope */
.envelope{left:228px;top:914px;width:338px;height:166px;background:var(--paper);border-bottom:6px solid var(--gold)}
.envelope svg{position:absolute;left:0;top:0}
.envelope .mark{position:absolute;left:0;right:0;top:8px;text-align:center}
.envelope .mark .brand-name{font-size:7px}

/* Compliment slip */
.slip{left:632px;top:914px;width:338px;height:166px;background:var(--black);border-bottom:6px solid var(--gold)}
.slip .mark{position:absolute;left:14px;top:20px;width:90px;text-align:center}
.slip .mark .brand-dot{width:13px;height:13px;margin-bottom:10px}
.slip .mark .brand-name{font-size:8px}
.slip .contact{position:absolute;left:0;bottom:8px;display:flex;gap:6px}
.slip .contact .bar{width:9px;background:var(--gold)}
.slip .contact .lines{font-family:var(--detail);font-size:5px;line-height:6.2px;color:var(--gold)}
</style>
</head>
<body>

<section class="piece letterhead">
  <div class="header-block">
    <span class="brand-dot"></span>
    <span class="brand-name">FARHAN JEWELLERS</span>
  </div>
  <div class="letter-body">
    <p>Dear [Recipient],</p>
    <p>We love the look of this stationery just the way it is. But you can add your own personal touch in almost no time.</p>
    <p>On the Design tab of the ribbon, check out the Themes, Colors, and Fonts galleries to preview different looks from a variety of choices. Then just click to apply the one you like.</p>
    <p>We’ve also created styles that let you match the formatting you see in this letter with just a click. On the Home tab of the ribbon, check out the Styles gallery for all styles used in this letter.</p>
    <p>Ready to add your digits? No problem. Just double-click the header area to add your contact information.</p>
    <p>Warm regards,<br>Saleem</p>
  </div>
  <div class="letter-footer">
    <span class="bar"></span>
    <div class="lines">
      14 Crescent Arcade, Gulberg Block, Lahore, Pakistan<br>
      042-35410278-80 &nbsp;|&nbsp; +92 333 815 6042<br>
      tariqnaveed@mailvora.com &nbsp;|&nbsp; www.farhanjewellers-pk.net
    </div>
  </div>
</section>

<section class="piece folder">
  <svg class="cut" width="509" height="679" viewBox="0 0 509 679">
    <polygon points="0,679 509,342 509,624 427,679" fill="var(--paper)"/>
  </svg>
  <div class="mark">
    <span class="brand-dot"></span>
    <span class="brand-name">FARHAN JEWELLERS</span>
  </div>
  <div class="site">www.farhanjewellers-pk.net</div>
</section>

<section class="piece card card-front">
  <svg width="195" height="113" viewBox="0 0 195 113">
    <path d="M60,0 C110,4 160,6 195,16 L195,0 Z" fill="var(--gold)"/>
    <path d="M0,72 C60,80 130,88 195,86 L195,113 L0,113 Z" fill="var(--gold)"/>
    <path d="M0,76 C60,84 130,92 195,90" stroke="var(--black)" stroke-width="1" fill="none"/>
  </svg>
  <div class="mark">
    <span class="brand-dot"></span>
    <span class="brand-name">FARHAN JEWELLERS</span>
  </div>
  <div class="person">
    <div class="name">Tariq Naveed</div>
    <div class="role">Business Development Consultant</div>
    <div class="line">042-35410278-80</div>
    <div class="line">+92 333 815 6042</div>
    <div class="line">tariqnaveed@mailvora.com</div>
    <div class="line">www.farhanjewellers-pk.net</div>
  </div>
  <div class="address">14 Crescent Arcade, Gulberg Block, Lahore, Pakistan</div>
</section>

<section class="piece card card-back">
  <svg width="195" height="113" viewBox="0 0 195 113">
    <path d="M40,0 C100,6 160,10 195,26 L195,0 Z" fill="var(--gold)"/>
    <path d="M0,96 C60,88 130,82 195,66 L195,113 L0,113 Z" fill="var(--gold)"/>
    <path d="M0,92 C60,84 130,78 195,62" stroke="var(--gold-light)" stroke-width="0.8" fill="none"/>
  </svg>
  <div class="mark">
    <span class="brand-dot"></span>
    <span class="brand-name">FARHAN JEWELLERS</span>
  </div>
  <div class="site">www.farhanjewellers-pk.net</div>
</section>

<section class="piece envelope">
  <svg width="338" height="40" viewBox="0 0 338 40">
    <polygon points="0,0 338,0 322,24 16,24" fill="var(--black)"/>
  </svg>
  <div class="mark"><span class="brand-name">FARHAN JEWELLERS</span></div>
</section>

<section class="piece slip">
  <div class="mark">
    <span class="brand-dot"></span>
    <span class="brand-name">FARHAN JEWELLERS</span>
  </div>
  <div class="contact">
    <span class="bar"></span>
    <div class="lines">
      14 Crescent Arcade, Gulberg Block, Lahore, Pakistan<br>
      042-35410278-80 &nbsp;|&nbsp; +92 333 815 6042<br>
      tariqnaveed@mailvora.com &nbsp;|&nbsp; www.farhanjewellers-pk.net
    </div>
  </div>
</section>

</body>
</html>
```